Roofing Company needs YOU to help put us on top!

Brightpeak Roofing, a fresh new company with quality and Innovation in mind, needs your help to stand out in the competitive Chicago market. With over 30 years of experience, all the right people and tools for the job, the only thing we are missing is your creative ideas in web design to help us grow our online presence.
Our Company offers exceptional quality at reasonable prices, we work for the everyday people both blue collar and white collar.

We have used Craftswarm in the past with multiple successful campaigns, we are excited to see what you can come up with for our website.

www.BrightpeakRoofing.example will be the domain

We will be hiring a photographer for visual content on our pages later. Stock photos are okay to use but should follow theme.

Thank you for taking the time on the submissions, if you have any questions don't hesitate to ask and we will provide whatever is needed to you.

Target Market(s)

Homeowners & Commercial Clients between 21-65

Industry/Entity Type

Roofing

Coding

Coded - Design and coding required

Number of Pages Required

4 page

Font styles to use
Sans Serif

Colors
ffffff
ec1f27
000000
5c5c5c
757575
b2b2b2

Requirements
Must have
• Color Scheme - should follow around our logo
• As for pages we were looking for an About, Services, Projects (gallery page) and Contact.
• Main page please include social media links and a a place so people could use tillbee to make payments
• Website should work on desktop as well as mobile platforms
Nice to have
• A Live chat feature would be nice if possible
Should not have
• Obscure Colors or Common web templates

```html
<!DOCTYPE html>
<html lang="en">
<head>
<meta charset="utf-8">
<title>Brightpeak Roofing</title>
<link href="https://fonts.googleapis.com/css2?family=Roboto:wght@300;400;500;700&display=swap" rel="stylesheet">
<style>
:root{
  --red:#ec1f27;
  --red-soft:#f0545a;
  --black:#000000;
  --ink:#111111;
  --dark:#1a1a1a;
  --grey-dark:#5c5c5c;
  --grey:#757575;
  --grey-light:#b2b2b2;
  --panel:#f3f3f3;
  --band:#f6f6f6;
  --white:#ffffff;
}
*{margin:0;padding:0;box-sizing:border-box}
html,body{width:669px;height:1200px;overflow:hidden;background:var(--white)}
body{font-family:'Roboto',sans-serif;color:var(--grey-dark);position:relative}
.abs{position:absolute}
.topbar{left:0;top:0;width:669px;height:20px;background:var(--ink);color:var(--white);font-size:7px}
.topbar .contact{position:absolute;top:6px;display:flex;align-items:center;gap:4px}
.square{width:14px;height:14px;background:#2a2a2a;border:1px solid #3a3a3a}
.topbar .socials{position:absolute;right:50px;top:3px;display:flex;gap:2px}
.navbar{left:0;top:20px;width:669px;height:44px;background:var(--white)}
.brand{font-weight:700;color:var(--black);font-size:13px;line-height:14px;display:flex;align-items:center;gap:5px}
.brand .dot{width:10px;height:10px;background:var(--red)}
.navbar .brand{position:absolute;left:50px;top:15px}
.nav a{position:absolute;top:19px;font-size:7.5px;color:var(--ink);text-decoration:none}
.nav a.active{color:var(--red)}
.hero-photo{left:0;top:64px}
.hero-title{left:83px;top:160px;color:var(--white);font-size:26px;font-weight:400}
.hero-sub{left:84px;top:190px;color:#e8e8e8;font-size:9.5px}
.btn{background:var(--red);color:var(--white);font-size:7px;display:flex;align-items:center;justify-content:center}
.arrow{width:18px;height:18px;display:flex;align-items:center;justify-content:center}
.estimate-form{left:85px;top:352px;width:155px;height:214px;background:var(--panel)}
.estimate-form .lead{position:absolute;left:0;width:155px;text-align:center;color:var(--ink)}
.field{position:absolute;left:11px;width:136px;background:var(--white);border:1px solid #e6e6e6;font-size:5.5px;color:var(--grey-light);padding:6px 7px}
.welcome-kicker{left:286px;top:409px;font-size:9.5px;color:var(--ink)}
.welcome-title{left:286px;top:420px;font-size:21px;color:var(--ink)}
.welcome-title span,.section-title span{color:var(--red)}
.welcome-text{left:286px;top:451px;width:334px;font-size:6.5px;line-height:12px;color:var(--grey-dark)}
.services-band{left:0;top:590px;width:669px;height:188px;background:var(--band)}
.section-title{left:0;width:669px;text-align:center;font-size:16px;color:var(--ink)}
.section-sub{left:0;width:669px;text-align:center;font-size:6.5px;line-height:11px;color:var(--grey)}
.service-card{top:670px;width:82px;height:78px;background:var(--white);border:1px solid #ececec;text-align:center;font-size:6.5px;color:var(--ink)}
.service-card svg{position:absolute;left:31px;top:22px}
.service-card .label{position:absolute;left:0;top:50px;width:80px}
.project{top:828px;width:141px;height:114px}
.project-label{left:336px;top:918px;width:141px;height:24px;background:var(--red);color:var(--white);font-size:8px;display:flex;align-items:center;justify-content:center}
.circle-btn{width:20px;height:20px;border-radius:50%;background:var(--white);display:flex;align-items:center;justify-content:center}
.cta{left:0;top:1004px;width:669px;height:50px;background:var(--red);color:var(--white)}
.footer{left:0;top:1054px;width:669px;height:146px;background:var(--dark);color:#b8b8b8;font-size:6.5px}
.footer h4{position:absolute;top:38px;font-size:10px;color:var(--white);font-weight:500}
.footer .link{position:absolute}
</style>
</head>
<body>

<div class="abs topbar">
  <div class="contact" style="left:50px">
    <svg width="7" height="7" viewBox="0 0 24 24"><path fill="#fff" d="M6.6 10.8a15.1 15.1 0 0 0 6.6 6.6l2.2-2.2c.3-.3.7-.4 1-.2 1.1.4 2.3.6 3.6.6.6 0 1 .4 1 1V20c0 .6-.4 1-1 1A17 17 0 0 1 3 4c0-.6.4-1 1-1h3.5c.6 0 1 .4 1 1 0 1.3.2 2.5.6 3.6.1.3 0 .7-.2 1z"/></svg>
    <span>555-014-0008</span>
  </div>
  <div class="contact" style="left:125px">
    <svg width="7" height="6" viewBox="0 0 24 18"><rect x="1" y="1" width="22" height="16" fill="#fff"/><path d="M1 1l11 9 11-9" stroke="#111" stroke-width="2" fill="none"/></svg>
    <span>info@brightpeakroofing.example</span>
  </div>
  <div class="socials"><div class="square"></div><div class="square"></div><div class="square"></div><div class="square"></div></div>
</div>

<div class="abs navbar">
  <div class="brand"><span class="dot"></span>Brightpeak Roofing</div>
  <svg class="abs" style="left:417px;top:0" width="10" height="5"><path d="M0 0h10L5 5z" fill="var(--red)"/></svg>
  <nav class="nav">
    <a class="active" style="left:416px">Home</a>
    <a style="left:456px">About</a>
    <a style="left:496px">Services</a>
    <a style="left:545px">Projects</a>
    <a style="left:593px">Contact</a>
  </nav>
</div>

<svg class="abs hero-photo" width="669" height="324" viewBox="0 0 669 324" role="img" aria-label="Silhouettes of roofers working on a roof against an evening sky">
  <defs>
    <linearGradient id="heroSky" x1="0" y1="0" x2="1" y2="1">
      <stop offset="0" stop-color="#5a5047"/>
      <stop offset="0.55" stop-color="#8a7c70"/>
      <stop offset="1" stop-color="#2a2420"/>
    </linearGradient>
  </defs>
  <polygon points="0,0 669,0 669,200 496,324 0,226" fill="url(#heroSky)"/>
</svg>
<div class="abs hero-title">Brightpeak Roofing</div>
<div class="abs hero-sub">&amp; Construction Company, Inc.</div>
<div class="abs btn" style="left:83px;top:210px;width:89px;height:20px;font-size:7.5px">Request An Estimate</div>
<div class="abs arrow" style="left:9px;top:174px;background:#444"><svg width="5" height="7"><path d="M4 0L0 3.5 4 7" stroke="#fff" fill="none"/></svg></div>
<div class="abs arrow" style="left:640px;top:174px;background:var(--red)"><svg width="5" height="7"><path d="M1 0l4 3.5L1 7" stroke="#fff" fill="none"/></svg></div>

<form class="abs estimate-form">
  <div class="lead" style="top:22px;font-size:7.5px">Request A Free</div>
  <div class="lead" style="top:32px;font-size:12.5px">Estimate From</div>
  <div class="field" style="top:48px;height:18px">Name*</div>
  <div class="field" style="top:70px;height:18px">Email*</div>
  <div class="field" style="top:92px;height:18px">Phone*</div>
  <div class="field" style="top:114px;height:18px">_ Select Service -
    <svg class="abs" style="right:6px;top:8px" width="5" height="3"><path d="M0 0h5L2.5 3z" fill="#999"/></svg></div>
  <div class="field" style="top:136px;height:40px">Comments</div>
  <div class="abs btn" style="left:11px;top:180px;width:136px;height:19px;font-weight:500;font-size:6.5px">SUBMIT NOW !</div>
</form>

<div class="abs welcome-kicker">Welcome To</div>
<div class="abs welcome-title">Brightpeak <span>Roofing</span></div>
<p class="abs welcome-text">Telling you about our company so you have a better understanding of who we are and how we operate and why you are making. We are a family owned, owner operated company as well as a Full-Time Professional Roofing Company. We have built our success by providing homeowners as well as small businesses in the entire Chicagoland and Greater Indiana area with quality work at competitive rates and providing the service you should expect from a quality roofing company.</p>
<div class="abs btn" style="left:286px;top:520px;width:71px;height:20px">View More Detail</div>

<section class="abs services-band"></section>
<div class="abs section-title" style="top:615px">Brightpeak <span>Services</span></div>
<div class="abs section-sub" style="top:640px">Lorem ipsum dolor sit amet, consectetuer adipiscing elit.<br>Aenean commodo ligula eget dolor.</div>

<div class="abs service-card" style="left:106px">
  <svg width="20" height="16"><rect x="0" y="6" width="11" height="9" fill="#111"/><circle cx="14" cy="6" r="4" stroke="var(--red)" stroke-width="2" fill="none"/><path d="M17 9l3 3" stroke="var(--red)" stroke-width="2"/></svg>
  <div class="label">Roof Inspections</div>
</div>
<div class="abs service-card" style="left:199px">
  <svg width="20" height="16"><rect x="1" y="5" width="17" height="11" fill="#111"/><rect x="4" y="9" width="3" height="3" fill="#fff"/><rect x="9" y="9" width="3" height="3" fill="#fff"/><rect x="3" y="0" width="4" height="4" fill="var(--red)"/></svg>
  <div class="label">Claims Assistance</div>
</div>
<div class="abs service-card" style="left:293px">
  <svg width="20" height="16"><path d="M10 0L1 8h3v8h12V8h3z" fill="#111"/><path d="M10 0L1 8h18z" fill="var(--red)"/><rect x="8" y="10" width="4" height="6" fill="#fff"/></svg>
  <div class="label">Residential Roofing</div>
</div>
<div class="abs service-card" style="left:387px">
  <svg width="20" height="16"><rect x="2" y="0" width="15" height="3" fill="var(--red)"/><rect x="2" y="3" width="15" height="13" fill="#111"/><path d="M5 5v10M9 5v10M13 5v10M2 8h15M2 12h15" stroke="#fff" stroke-width="1"/></svg>
  <div class="label">Commerical Roofing</div>
</div>
<div class="abs service-card" style="left:480px">
  <svg width="20" height="16"><rect x="0" y="7" width="11" height="9" fill="#111"/><path d="M9 3l9 9" stroke="var(--red)" stroke-width="3"/><circle cx="9" cy="3" r="3" fill="var(--red)"/></svg>
  <div class="label">Roof Repairs</div>
</div>

<div class="abs section-title" style="top:800px">Our <span>Projects</span></div>
<div class="abs project" style="left:50px;background:linear-gradient(135deg,#e8ecef,#9aa3ab)" role="img" aria-label="Modern white building with a glass tower"></div>
<div class="abs project" style="left:194px;background:linear-gradient(180deg,#3a8fe0 0%,#5aa6ee 45%,#a4553a 70%,#7c3a26 100%)" role="img" aria-label="Terracotta roof tiles and brick chimneys under a blue sky"></div>
<div class="abs project" style="left:336px;background:linear-gradient(160deg,#9aa4ad,#4a4640 60%,#6a3d30)" role="img" aria-label="Roofers laying shingles on a residential roof"></div>
<div class="abs project" style="left:479px;background:linear-gradient(180deg,#6a6a66,#b4b2aa 60%,#8a8882)" role="img" aria-label="Two workers in hard hats inspecting a concrete floor"></div>
<div class="abs project-label">Residential Roofing</div>
<div class="abs circle-btn" style="left:383px;top:870px"><svg width="8" height="8"><circle cx="3.2" cy="3.2" r="2.5" stroke="#111" fill="none"/><path d="M5 5l2.5 2.5" stroke="#111"/></svg></div>
<div class="abs circle-btn" style="left:406px;top:870px"><svg width="8" height="8"><path d="M3 5l2-2" stroke="var(--red)"/><rect x="0.5" y="3.5" width="4" height="3" rx="1.5" transform="rotate(-45 2.5 5)" stroke="var(--red)" fill="none"/><rect x="3.5" y="0.5" width="4" height="3" rx="1.5" transform="rotate(-45 5.5 2)" stroke="var(--red)" fill="none"/></svg></div>
<div class="abs btn" style="left:297px;top:956px;width:76px;height:21px;font-size:6px">View All Projects</div>

<section class="abs cta">
  <div class="abs" style="left:49px;top:18px;font-size:8px">Contact Price</div>
  <div class="abs" style="left:49px;top:28px;font-size:12px">Roofing today For a Free Estimate</div>
  <div class="abs" style="left:438px;top:20px;font-size:10px;display:flex;align-items:center;gap:5px">
    <svg width="9" height="9" viewBox="0 0 24 24"><path fill="#fff" d="M6.6 10.8a15.1 15.1 0 0 0 6.6 6.6l2.2-2.2c.3-.3.7-.4 1-.2 1.1.4 2.3.6 3.6.6.6 0 1 .4 1 1V20c0 .6-.4 1-1 1A17 17 0 0 1 3 4c0-.6.4-1 1-1h3.5c.6 0 1 .4 1 1 0 1.3.2 2.5.6 3.6.1.3 0 .7-.2 1z"/></svg>
    555-014-0008
  </div>
  <div class="abs btn" style="left:523px;top:17px;width:96px;height:19px;background:var(--red-soft);font-size:5.8px">REQUEST AN ESTIMATE</div>
</section>

<footer class="abs footer">
  <div class="brand" style="position:absolute;left:50px;top:36px;color:var(--white);font-size:13px"><span class="dot"></span>Brightpeak Roofing</div>
  <div class="abs" style="left:65px;top:54px;color:var(--white);font-size:9px;font-weight:700">555-014-0008</div>

  <h4 style="left:186px">Quick Links</h4>
  <span class="link" style="left:186px;top:59px">Home</span>
  <span class="link" style="left:186px;top:72px">About Us</span>
  <span class="link" style="left:186px;top:86px">Service</span>
  <span class="link" style="left:186px;top:100px">Roof Types</span>
  <span class="link" style="left:256px;top:59px">Commerical</span>
  <span class="link" style="left:256px;top:72px">Residential</span>
  <span class="link" style="left:256px;top:86px">Repair</span>
  <span class="link" style="left:256px;top:100px">Contact Us</span>

  <h4 style="left:339px">Contact Info</h4>
  <span class="link" style="left:339px;top:59px;width:110px;line-height:10px">Brightpeak Roofing &amp; Construction Company, Inc.</span>
  <span class="link" style="left:339px;top:86px"><span style="color:var(--red)">&#9679;</span>&nbsp; Illinois &nbsp;&nbsp;555-014-0008</span>
  <span class="link" style="left:339px;top:100px"><span style="color:var(--red)">&#9679;</span>&nbsp; Indiana &nbsp;&nbsp;555-019-0208</span>

  <div class="abs" style="left:542px;top:33px;display:flex;gap:4px">
    <div class="square" style="width:16px;height:16px;background:#111;border-color:#333"></div>
    <div class="square" style="width:16px;height:16px;background:#111;border-color:#333"></div>
    <div class="square" style="width:16px;height:16px;background:#111;border-color:#333"></div>
    <div class="square" style="width:16px;height:16px;background:#111;border-color:#333"></div>
  </div>
  <div class="abs" style="right:50px;top:65px;text-align:right;line-height:10px">Copyright 2016<br>Brightpeak Roofing | All Right Reserved</div>
  <div class="abs" style="left:594px;top:88px;width:25px;height:15px;background:#f2e6b8;color:#333;font-size:5.5px;display:flex;align-items:center;justify-content:center">tillbee</div>

  <div class="abs" style="left:605px;top:114px;width:24px;height:24px;border-radius:50%;background:var(--red);display:flex;align-items:center;justify-content:center">
    <svg width="10" height="9"><rect x="0.5" y="0.5" width="9" height="6" rx="1.5" stroke="#fff" fill="none"/><path d="M3 6.5L2.5 8.5 5 6.5" stroke="#fff" fill="none"/></svg>
  </div>
  <div class="abs" style="left:633px;top:119px;color:var(--white);font-size:5.5px;line-height:6px">Live<br><span style="font-size:10px">Chat</span></div>
</footer>

</body>
</html>
```